Velmor PashuのRTZの電子書籍表紙デザインをお願いします。

*週末ごとに和みを探す読者へ贈る癒やしの四季手帳*というタイトルの表紙デザインの発注です。
サブタイトル 猫の昼寝は街を照らす
猫の昼寝は毎日を照らす
私は猫の昼寝に癒された
になります。
お笑い要素の多い1日1笑いみたいな本の表紙です。

初めての表紙デザイン依頼なので、よく勝手がわかっていませんので、
出来上がったデザインを作家グループの中で投票にかけて、
一番投票得票数の多かったものを表紙デザインとして選ばせていただきたいと考えております。
もしかしたら、その中で、何か修正依頼など来るかもしれませんが、
それも含めて、ご対応していただける方よろしくお願いします。

1部内容の抜粋を記載します。

その他何かご不明な点がございましたら、お気軽にご質問下さい。
よろしくお願いいたします。
すいません。作家名は後でお伝えします。作家名もどこかに挿入いただきたいです。よろしくお願いします。
データサイズですが、推奨サイズでJPEGファイルでご納品下さい、よろしくお願いします。
皆様、たくさんのご応募まことにありがとうございました。
現在、作家グループへ全体回覧のメールを致しました。
皆様の投票結果までお待ちください。
また、この度、いろいろな作品に触れさせていただきましたこと本当に
本当に感謝いたします。
今回の表紙に関しましては、どうしても1名しか選べない状況がございますこと
また、選挙による投票にて決定致しますこと、ご理解何卒よろしくお願い申しあげます。
また、もしも、今回当選に至らないことがありましても、
今後も私自身は作家生活を継続予定ですので、
(今回は作品の表紙に合わないことがあっても)作風の気に入ったデザイナー様には
個人的にお話を相談させていただく場合もあると思っております。
その際には何卒よろしくお願い申し上げます。この度はまことにありがとうございました。
この度はご応募まことにありがとうございました。厳選なる選挙の結果、1名の作家さんが選ばれました。
選ばれました方には個別にお伝えいたしております。この度はまことにご応募ありがとうございました。

作家メンバーによる総選挙にて決定させて頂きました。皆様に広く愛される作品で、投票数も多く選ばせて頂きました。誠にありがとうございました。

今回、誠にご提案ありがとうございました。私自身は作家活動を継続していくつもりですので、また、個別にご依頼させて頂くこともあるかと思います。その時はよろしくお願いします。この度はありがとうございました。

```html
<!DOCTYPE html>
<html lang="ja">
<head>
<meta charset="utf-8">
<title>週末ごとに和みを探す読者へ贈る癒やしの四季手帳</title>
<link rel="stylesheet" href="https://fonts.googleapis.com/css2?family=Noto+Sans+JP:wght@700;900&display=swap">
<style>
  :root{
    --ink:#1a1a1a;
    --red:#e02020;
    --white:#ffffff;
    --pink:#ef6fae;
    --yellow:#f7e04a;
    --green:#8fd36a;
    --sky:#6fb8ee;
    --cal-blue:#3f86c9;
    --cal-bg:#eef4fa;
    --skin:#f2c6a8;
    --shirt:#ee6a86;
    --jeans:#3e6fc0;
  }
  *{margin:0;padding:0;box-sizing:border-box}
  html,body{width:750px;height:1200px;overflow:hidden;background:var(--white)}
  .cover{position:relative;width:750px;height:1200px;overflow:hidden;font-family:"Noto Sans JP",sans-serif;color:var(--ink);background:var(--cal-bg)}
  .burst-backdrop{position:absolute;left:0;top:0;width:750px;height:590px;
    background:linear-gradient(135deg,var(--pink) 0%,var(--yellow) 35%,var(--green) 65%,var(--sky) 100%)}
  .bubble{position:absolute}
  .bubble svg{position:absolute;inset:0}
  .bubble p{position:absolute;inset:0;display:flex;align-items:center;justify-content:center;text-align:center;font-weight:700;font-size:29px;line-height:1.25}
  .bubble-left{left:10px;top:14px;width:200px;height:135px}
  .bubble-mid{left:165px;top:80px;width:215px;height:150px}
  .bubble-right{left:550px;top:4px;width:200px;height:140px}
  .title-panel{position:absolute;left:45px;top:230px;width:680px;height:300px;background:var(--white);border:4px solid var(--ink)}
  .title-top{position:absolute;top:12px;left:0;width:100%;text-align:center;font-weight:900;font-size:46px;line-height:1}
  .title-top .accent{color:var(--red)}
  .title-line{position:absolute;left:0;width:100%;text-align:center;font-weight:900;line-height:1;white-space:nowrap}
  .line1{top:72px;font-size:54px;letter-spacing:-1px}
  .line2{top:142px;font-size:72px}
  .line2 .accent{color:var(--red)}
  .line3{top:222px;font-size:68px;text-align:left;padding-left:120px}
  .author{position:absolute;right:40px;top:238px;display:flex;gap:4px}
  .author span{width:44px;height:44px;border-radius:50%;background:var(--red);color:var(--white);font-weight:900;font-size:28px;display:flex;align-items:center;justify-content:center}
  .calendar{position:absolute;left:30px;top:570px;width:700px;display:grid;grid-template-columns:repeat(5,128px);column-gap:15px;row-gap:14px}
  .day{height:128px;background:var(--white);border:3px solid var(--ink);display:flex;flex-direction:column}
  .day-head{height:30px;background:var(--cal-blue);border-bottom:3px solid var(--ink);display:flex;justify-content:space-around;align-items:center}
  .day-head i{width:8px;height:22px;border-radius:4px;background:var(--white);border:2px solid var(--ink);margin-top:-18px}
  .day-num{flex:1;display:flex;align-items:center;justify-content:center;font-weight:900;font-size:56px}
  .day-num svg{width:60px;height:60px}
  .figure{position:absolute;left:165px;top:580px;width:445px;height:620px;border-radius:200px 200px 40px 40px;
    background:linear-gradient(180deg,var(--skin) 0%,var(--shirt) 40%,var(--jeans) 80%,var(--skin) 100%);opacity:.96}
</style>
</head>
<body>
<main class="cover">
  <div class="burst-backdrop" role="img" aria-label="ピンク・黄・緑・水色のコマ割りと集中線のポップな漫画風背景"></div>

  <div class="bubble bubble-left">
    <svg viewBox="0 0 200 135"><ellipse cx="100" cy="67" rx="96" ry="62" fill="#fff" stroke="#1a1a1a" stroke-width="3"/></svg>
    <p>猫の昼寝は<br>街を照らす</p>
  </div>
  <div class="bubble bubble-mid">
    <svg viewBox="0 0 215 150"><ellipse cx="107" cy="75" rx="103" ry="70" fill="#fff" stroke="#1a1a1a" stroke-width="3"/></svg>
    <p>猫の昼寝は<br>毎日を照らす</p>
  </div>
  <div class="bubble bubble-right">
    <svg viewBox="0 0 200 140"><ellipse cx="100" cy="70" rx="96" ry="66" fill="#fff" stroke="#1a1a1a" stroke-width="3"/></svg>
    <p>私は猫の昼寝<br>に癒された</p>
  </div>

  <section class="title-panel">
    <h1>
      <span class="title-top"><span class="accent">週末</span>ごとに</span>
      <span class="title-line line1">和みを探す読者へ贈る</span>
      <span class="title-line line2">癒<span class="accent">や</span>しの四季</span>
      <span class="title-line line3">手帳</span>
    </h1>
    <div class="author"><span>著</span><span>者</span></div>
  </section>

  <section class="calendar">
    <div class="day"><div class="day-head"><i></i><i></i></div><div class="day-num">16</div></div>
    <div class="day"><div class="day-head"><i></i><i></i></div><div class="day-num">17</div></div>
    <div class="day"><div class="day-head"><i></i><i></i></div><div class="day-num">18</div></div>
    <div class="day"><div class="day-head"><i></i><i></i></div><div class="day-num">19</div></div>
    <div class="day"><div class="day-head"><i></i><i></i></div><div class="day-num">20</div></div>
    <div class="day"><div class="day-head"><i></i><i></i></div><div class="day-num">21</div></div>
    <div class="day"><div class="day-head"><i></i><i></i></div><div class="day-num">22</div></div>
    <div class="day"><div class="day-head"><i></i><i></i></div><div class="day-num">23</div></div>
    <div class="day"><div class="day-head"><i></i><i></i></div><div class="day-num">24</div></div>
    <div class="day"><div class="day-head"><i></i><i></i></div><div class="day-num">25</div></div>
    <div class="day"><div class="day-head"><i></i><i></i></div><div class="day-num">26</div></div>
    <div class="day"><div class="day-head"><i></i><i></i></div><div class="day-num">27</div></div>
    <div class="day"><div class="day-head"><i></i><i></i></div><div class="day-num">28</div></div>
    <div class="day"><div class="day-head"><i></i><i></i></div><div class="day-num">29</div></div>
    <div class="day"><div class="day-head"><i></i><i></i></div><div class="day-num">30</div></div>
    <div class="day"><div class="day-head"><i></i><i></i></div><div class="day-num">31</div></div>
    <div class="day"><div class="day-head"><i></i><i></i></div><div class="day-num"><svg viewBox="0 0 60 60"><path d="M10 32 L25 46 L52 14" fill="none" stroke="#1a1a1a" stroke-width="8" stroke-linecap="round" stroke-linejoin="round"/></svg></div></div>
    <div class="day"><div class="day-head"><i></i><i></i></div><div class="day-num"><svg viewBox="0 0 60 60"><circle cx="30" cy="30" r="22" fill="none" stroke="#1a1a1a" stroke-width="7"/></svg></div></div>
    <div class="day"><div class="day-head"><i></i><i></i></div><div class="day-num"><svg viewBox="0 0 60 60"><path d="M12 12 L48 48 M48 12 L12 48" stroke="#1a1a1a" stroke-width="8" stroke-linecap="round"/></svg></div></div>
    <div class="day"><div class="day-head"><i></i><i></i></div><div class="day-num"><svg viewBox="0 0 60 60" fill="#1a1a1a"><rect x="6" y="8" width="48" height="8"/><rect x="6" y="22" width="10" height="8"/><rect x="19" y="22" width="10" height="8"/><rect x="32" y="22" width="10" height="8"/><rect x="45" y="22" width="9" height="8"/><rect x="6" y="34" width="10" height="8"/><rect x="19" y="34" width="10" height="8"/><rect x="32" y="34" width="10" height="8"/><rect x="45" y="34" width="9" height="8"/><rect x="6" y="46" width="10" height="8"/><rect x="19" y="46" width="10" height="8"/><rect x="32" y="46" width="10" height="8"/><rect x="45" y="46" width="9" height="8"/></svg></div></div>
  </section>

  <div class="figure" role="img" aria-label="カレンダーの前で膝を抱えて座り、指をさして大笑いする女性のイラスト"></div>
</main>
</body>
</html>
```